Quiet Harbor Podcast Business Card Design

Needing a business card with the logo design provided for Quiet Harbor Podcast. I am looking for a modern style that fits the current logo.

Info:
Name: Teodor Vask
Title: Creator/Host
Email: teodor@quietharborcast.com
Phone: (555) 274-9163
www.quietharborcast.com
Twitter: @qharborcast
Instagram: @quietharborcastshow
Facebook: Quiet Harbor Podcast

Industry/Entity Type

Business

Font styles to use
Sans Serif

Colors
000000
ffffff

Requirements
Must have
• modern, clean design
Nice to have
• social media contact info

```html
<!DOCTYPE html>
<html lang="en">
<head>
<meta charset="utf-8">
<title>Quiet Harbor Podcast – Business Cards</title>
<link rel="stylesheet" href="https://fonts.googleapis.com/css2?family=Roboto+Condensed:wght@300;400;700&display=swap">
<style>
  :root {
    --card-black: #1f1c1c;
    --ink-white: #ffffff;
    --muted-white: #d9d9d9;
    --divider: #6a6666;
    --backdrop: #e9e6e1;
  }
  * { margin: 0; padding: 0; box-sizing: border-box; }
  html, body { width: 1200px; height: 1200px; overflow: hidden; }
  body {
    background: var(--backdrop);
    font-family: "Roboto Condensed", Arial, sans-serif;
    display: flex;
    flex-direction: column;
    align-items: center;
    justify-content: center;
    gap: 70px;
  }
  .card {
    width: 700px;
    height: 400px;
    background: var(--card-black);
    color: var(--ink-white);
    box-shadow: 0 6px 18px rgba(0,0,0,0.18);
    position: relative;
  }
  .brand {
    display: flex;
    flex-direction: column;
    align-items: center;
  }
  .brand-mark {
    width: 70px;
    height: 70px;
    background: var(--ink-white);
    margin-bottom: 18px;
  }
  .brand-name {
    font-weight: 700;
    font-size: 40px;
    letter-spacing: 0.5px;
    text-transform: uppercase;
    line-height: 1;
    text-align: center;
  }
  .brand-sub {
    font-weight: 700;
    font-size: 15px;
    letter-spacing: 9px;
    text-transform: uppercase;
    margin-top: 6px;
    padding-left: 9px;
  }

  /* Back side */
  .card-back {
    display: flex;
    flex-direction: column;
    align-items: center;
    justify-content: center;
  }
  .socials {
    margin-top: 26px;
    text-align: center;
    font-weight: 300;
    font-size: 19px;
    line-height: 1.6;
    color: var(--muted-white);
  }

  /* Front side */
  .card-front {
    display: flex;
    align-items: center;
  }
  .card-front .brand {
    width: 370px;
    padding-top: 30px;
  }
  .card-front .brand-mark { width: 60px; height: 60px; }
  .card-front .brand-name { font-size: 34px; }
  .card-front .brand-sub { font-size: 13px; letter-spacing: 8px; }
  .divider {
    width: 1px;
    height: 170px;
    background: var(--divider);
    margin-top: -30px;
  }
  .contact {
    padding-left: 34px;
    margin-top: -40px;
  }
  .person-name {
    font-weight: 300;
    font-size: 34px;
    text-transform: uppercase;
    line-height: 1;
  }
  .person-title {
    font-weight: 300;
    font-size: 18px;
    color: var(--muted-white);
    margin: 6px 0 24px 30px;
  }
  .contact-list { list-style: none; margin-left: 30px; }
  .contact-list li {
    display: flex;
    align-items: center;
    gap: 8px;
    font-weight: 300;
    font-size: 18px;
    line-height: 1.5;
    color: var(--muted-white);
  }
  .icon {
    width: 18px;
    height: 18px;
    flex: none;
  }
</style>
</head>
<body>

  <section class="card card-back">
    <div class="brand">
      <div class="brand-mark"></div>
      <div class="brand-name">Quiet Harbor</div>
      <div class="brand-sub">Podcast</div>
    </div>
    <div class="socials">
      <p>TW: @qharborcast</p>
      <p>FB: Quiet Harbor Podcast | INS: @quietharborcastshow</p>
    </div>
  </section>

  <section class="card card-front">
    <div class="brand">
      <div class="brand-mark"></div>
      <div class="brand-name">Quiet Harbor</div>
      <div class="brand-sub">Podcast</div>
    </div>
    <div class="divider"></div>
    <div class="contact">
      <p class="person-name">Teodor Vask</p>
      <p class="person-title">Creator/ Host</p>
      <ul class="contact-list">
        <li>
          <svg class="icon" viewBox="0 0 18 18" aria-hidden="true">
            <rect width="18" height="18" rx="3" fill="#fff"/>
            <path d="M4 7.5c0-2 2.2-3 5-3s5 1 5 3l-2 .4-.4-1.5H6.4L6 7.9z" fill="#1f1c1c"/>
            <rect x="5" y="9" width="8" height="5" rx="1" fill="#1f1c1c"/>
          </svg>
          (555) 274-9163
        </li>
        <li>
          <svg class="icon" viewBox="0 0 18 18" aria-hidden="true">
            <rect width="18" height="18" rx="3" fill="#fff"/>
            <circle cx="9" cy="9" r="5" fill="none" stroke="#1f1c1c" stroke-width="1.2"/>
            <ellipse cx="9" cy="9" rx="2.2" ry="5" fill="none" stroke="#1f1c1c" stroke-width="1"/>
            <line x1="4" y1="9" x2="14" y2="9" stroke="#1f1c1c" stroke-width="1"/>
          </svg>
          www.quietharborcast.com
        </li>
        <li>
          <svg class="icon" viewBox="0 0 18 18" aria-hidden="true">
            <rect width="18" height="18" rx="3" fill="#fff"/>
            <rect x="4" y="5.5" width="10" height="7" fill="none" stroke="#1f1c1c" stroke-width="1.2"/>
            <path d="M4 5.5l5 4 5-4" fill="none" stroke="#1f1c1c" stroke-width="1.2"/>
          </svg>
          teodor@quietharborcast.com
        </li>
      </ul>
    </div>
  </section>

</body>
</html>
```